BRVL Brochure Design

Northfield Council of Clinical Standards (BRVL) needs a whole new brochure. I've upload EPS logos and past brochures. Our tagline is to "modernize healthcare" and we think our brochure should reflect that, so that's the purpose of this project.

BRVL is a proven leader in healthcare education, training and
consulting services for health professionals. We’ve earned a reputation for excellence in healthcare quality improvement and management.

BRVL works to improve healthcare quality by educating healthcare professionals about healthcare best practices. We focus on instructing our clients on how to plan for, measure, and improve healthcare quality in all facilities and facets such as:

Patient Safety
Infection Control
Performance Improvement
Risk Management
Compliance and Accreditation
Health and Hospital Administration
Health Insurance
Healthcare Financial Management
Facility Management and Safety

DESIGN SUGGESTIONS:

Brochure Size: 8.5 X 11 full size brochure or 8.5 X 11 trifold brochure

Number of Pages: 2 to 3

Colors: Feel free to use a wide array of colors but try to stay away from colors that are too loud, ex: Pink, Purple, Neon Green.

Themes: Professional, Educational

Designs:

Pelor by Oskar Lindqvist

Quorvo Pamphlet by Derek Malloway

Lanterns for harvest by Solvendri

Paisaje de Sr KT by vrpl

http://www.plimbask.com/post/28461937205/10-creative-brochure-designs

Don't limit yourself to these examples. However, these are examples we liked

Reason: We would like to see more designs

We want more full page designs than tri-fold 

We are considering both tri-fold and full-page but would like to see more full page designs 

Reason: Our lead designer making the decisions on this project has been fired. I apologize for the inconvenience. We want extend the project one last time

Target Market(s)

Students, Doctors, and Educational Professionals

Industry/Entity Type

Healthcare

Logo Text

asdfasdf

Font styles to use
Serif
Sans Serif
Decorative
Script

Requirements
Should not have
• Pink, Purple, Neon Green colors

```html
<!DOCTYPE html>
<html lang="en">
<head>
<meta charset="utf-8">
<title>BRVL Brochure</title>
<link href="https://fonts.googleapis.com/css2?family=Open+Sans:wght@400;600;700&family=Oswald:wght@300;400;500&display=swap" rel="stylesheet">
<style>
  :root {
    --page-bg: #eceae6;
    --paper: #ffffff;
    --navy: #0d3f73;
    --blue: #1a6fb5;
    --sky: #3d9ad9;
    --pale: #d7e9f6;
    --ink: #2b2f36;
    --muted: #5d6672;
    --accent: #8fd0f5;
  }
  * { box-sizing: border-box; margin: 0; padding: 0; }
  html, body { width: 744px; height: 1200px; overflow: hidden; }
  body { background: var(--page-bg); font-family: "Open Sans", sans-serif; color: var(--ink); position: relative; }

  .cover {
    position: absolute; left: 232px; top: 30px; width: 280px; height: 720px;
    background: var(--paper); box-shadow: 0 4px 14px rgba(0,0,0,.18);
    display: flex; flex-direction: column; overflow: hidden;
  }
  .brand { display: flex; align-items: center; gap: 8px; }
  .brand-mark { width: 18px; height: 18px; border-radius: 50%; background: var(--sky); }
  .brand-name { font-family: "Open Sans", sans-serif; font-weight: 700; color: var(--navy); letter-spacing: 1px; }
  .brand-sub { font-size: 7px; line-height: 1.2; color: var(--muted); max-width: 90px; }
  .cover .brand { padding: 22px 20px 16px; justify-content: center; }
  .cover .brand-name { font-size: 30px; }
  .cover-tag {
    background: var(--navy); color: #fff; font-family: "Oswald", sans-serif;
    font-size: 13px; letter-spacing: 2px; text-align: center; padding: 6px 0;
  }
  .cover-photo { height: 250px; background: linear-gradient(135deg, #e9eff4 0%, #c8d6e2 55%, #8aa6bf 100%); }
  .cover-band {
    background: linear-gradient(180deg, var(--blue), var(--navy));
    color: #fff; padding: 22px 20px; flex: 1; position: relative;
  }
  .cover-headline { font-family: "Oswald", sans-serif; font-weight: 300; font-size: 25px; line-height: 1.15; text-transform: uppercase; }
  .cover-headline strong { font-weight: 500; color: var(--accent); }
  .cover-band svg { position: absolute; left: 0; bottom: 0; }

  .spread {
    position: absolute; left: 27px; top: 780px; width: 690px; height: 400px;
    background: var(--paper); box-shadow: 0 4px 14px rgba(0,0,0,.18);
    display: flex; overflow: hidden;
  }
  .panel { width: 345px; padding: 14px 16px; font-size: 7.2px; line-height: 1.45; }
  .panel + .panel { border-left: 1px solid #e1e6ec; }
  .intro { background: var(--blue); color: #fff; padding: 9px 10px; margin: -14px -16px 10px; }
  .section-bar {
    display: flex; align-items: center; gap: 6px;
    font-family: "Oswald", sans-serif; font-size: 12px; letter-spacing: 1px; color: var(--navy);
    border-bottom: 2px solid var(--sky); padding-bottom: 3px; margin-bottom: 8px; text-transform: uppercase;
  }
  .course { margin-bottom: 7px; }
  .course h4 { font-size: 7.5px; color: var(--blue); font-weight: 700; text-transform: uppercase; }
  .course .cost { color: var(--sky); font-weight: 600; }
  .panel-right .brand { margin-bottom: 10px; }
  .panel-right .brand-name { font-size: 20px; }
  .mission h3 { font-family: "Oswald", sans-serif; font-size: 11px; color: var(--navy); margin: 8px 0 4px; }
  .mission li { list-style: none; font-weight: 700; color: var(--blue); font-size: 7.5px; }
  .mission li::before { content: "\25A0  "; color: var(--sky); }
  .quote { background: var(--navy); color: #fff; padding: 10px; margin-top: 10px; font-style: italic; }
  p + p { margin-top: 5px; }
</style>
</head>
<body>

<section class="cover">
  <div class="brand">
    <span class="brand-mark"></span>
    <span class="brand-name">BRVL</span>
    <span class="brand-sub">Northfield Council of Clinical Standards</span>
  </div>
  <div class="cover-tag">MODERNIZE HEALTHCARE</div>
  <div class="cover-photo" role="img" aria-label="Healthcare professional in a white coat, softly blurred"></div>
  <div class="cover-band">
    <h1 class="cover-headline">The <strong>highest quality</strong> in healthcare comes from the <strong>highest</strong> quality people</h1>
    <svg width="280" height="120" viewBox="0 0 280 120" aria-hidden="true">
      <path d="M0 90 Q140 30 280 70" fill="none" stroke="rgba(255,255,255,.25)" stroke-width="2"/>
      <path d="M0 110 Q140 50 280 90" fill="none" stroke="rgba(255,255,255,.15)" stroke-width="2"/>
    </svg>
  </div>
</section>

<section class="spread">
  <div class="panel panel-left">
    <div class="intro">BRVL certificate courses are designed to impart advanced knowledge that will help you plan, measure and improve quality in your facility. Whether you are a student or an experienced clinician, our courses support your path to better patient care.</div>
    <div class="section-bar">Certification Courses</div>
    <p>BRVL courses can be taken for your personal and professional growth. Each course is recognized by our board and ends with a final exam and certificate.</p>
    <div class="course">
      <h4>Certificate in Healthcare Quality</h4>
      <p>This course covers the principles of planning, measuring and improving quality across all clinical settings and services.</p>
      <p class="cost">Cost of course: $495</p>
    </div>
    <div class="course">
      <h4>Certified Professional in Infection Control</h4>
      <p>Learn prevention strategies, surveillance methods and safe practice standards for any healthcare facility.</p>
      <p class="cost">Cost of course: $395</p>
    </div>
    <div class="course">
      <h4>Certificate in Performance Improvement</h4>
      <p>Build skills in data review, risk management and accreditation readiness for modern organizations.</p>
      <p class="cost">Cost of course: $450</p>
    </div>
  </div>

  <div class="panel panel-right">
    <div class="brand">
      <span class="brand-mark"></span>
      <span class="brand-name">BRVL</span>
      <span class="brand-sub">Northfield Council of Clinical Standards</span>
    </div>
    <div class="section-bar">About Us</div>
    <p>Here at the Northfield Council of Clinical Standards, we believe that the highest quality in healthcare comes from the highest quality people. We provide a learning environment focused on quality and led by expert professionals.</p>
    <div class="mission">
      <h3>OUR MISSION</h3>
      <ul>
        <li>Quality in all that we do</li>
        <li>Integrity in all of our work</li>
        <li>Innovation in training and education</li>
        <li>Leadership worldwide</li>
        <li>Continuous education</li>
      </ul>
    </div>
    <p>Our mission is to improve quality in healthcare by educating the professionals who work in it every day, so that patients receive safer and better care.</p>
    <div class="quote">"Earning my certificate gave me the tools to lead quality projects at my hospital. The courses were clear, practical and worth every hour."<br>— Course Graduate, Nurse Manager</div>
  </div>
</section>

</body>
</html>
```